Brightmoor Cleaning Services

need a brochure for my cleaning company. Contact info coming soon .

Target Market(s)

Cleaning Services

Industry/Entity Type

Cleaning Service

Requirements
Must have
• I attached logo for you to use.

Corporate address -
472 Kestrel Ridge W Ste 518
Fernhollow, OR 98102

Phone number - 877-514-SHINE
Nice to have
• bifold brochure. I attached some samples
Should not have
• Pictures of people. Keep it clean and professional.

```html
<!DOCTYPE html>
<html lang="en">
<head>
<meta charset="utf-8">
<title>Brightmoor Cleaning Services – Trifold Brochure</title>
<link href="https://fonts.googleapis.com/css2?family=Oswald:wght@500;600;700&family=Open+Sans:wght@400;600;700&display=swap" rel="stylesheet">
<style>
:root{
  --blue:#1f4fa8;
  --blue-dark:#173d8a;
  --red:#e0252b;
  --red-dark:#b81a20;
  --white:#ffffff;
  --paper:#f7f8fb;
  --ink:#1d2b4f;
  --stage:#e4e5e7;
}
*{box-sizing:border-box;margin:0;padding:0}
html,body{width:1200px;height:2400px;overflow:hidden;background:var(--stage)}
body{position:relative;font-family:"Open Sans",Arial,sans-serif;color:var(--ink)}
.spread{position:absolute;left:45px;width:1110px;height:860px;display:flex;background:var(--white);box-shadow:0 6px 24px rgba(0,0,0,.18)}
.spread--outside{top:250px}
.spread--inside{top:1290px}
.panel{position:relative;width:370px;height:860px;overflow:hidden;background:var(--paper)}
.panel + .panel{border-left:1px solid rgba(0,0,0,.06)}
.panel svg.band{position:absolute;left:0;width:370px;display:block}
.photo{position:absolute;left:0;width:370px}
.heading{font-family:"Oswald",Arial,sans-serif;font-weight:700;text-transform:uppercase;letter-spacing:.5px}
.body-text{font-size:12.5px;line-height:1.55}
.logo{position:absolute;display:flex;align-items:center;gap:10px;font-family:"Open Sans",Arial,sans-serif;font-weight:700;color:var(--blue);font-size:20px;line-height:1.1}
.logo__dot{width:30px;height:30px;border-radius:50%;background:var(--red);flex:none}
.phone-pill{position:absolute;display:flex;align-items:center;gap:10px;background:var(--red);color:var(--white);border-radius:28px;font-family:"Oswald",Arial,sans-serif;font-weight:600;font-size:26px;padding:6px 22px 6px 8px;letter-spacing:.5px;white-space:nowrap}
.phone-pill__icon{width:36px;height:36px;border-radius:50%;background:var(--white);display:flex;align-items:center;justify-content:center}

/* outside left */
.reliable__title{position:absolute;top:300px;left:34px;font-size:22px;color:var(--red)}
.reliable__title span{color:var(--blue)}
.feature{position:absolute;left:34px;width:305px;display:flex;gap:12px}
.feature__icon{width:26px;height:26px;border-radius:4px;background:var(--red);flex:none;margin-top:2px}
.feature__name{font-weight:700;font-size:13px;color:var(--red);text-transform:uppercase}
.feature p{font-size:11.5px;line-height:1.5}
.tagline{position:absolute;left:24px;bottom:36px;color:var(--white);font-size:20px;font-weight:600;line-height:1.2}

/* outside middle */
.contact__circle{position:absolute;top:38px;left:115px;width:140px;height:140px;border-radius:50%;border:5px solid var(--white);background:radial-gradient(circle at 50% 60%,#8c8f99,#b9bcc4 55%,#d9dbe0)}
.contact__title{position:absolute;top:236px;width:100%;text-align:center;font-size:26px;color:var(--blue)}
.contact__text{position:absolute;top:284px;left:36px;width:298px;text-align:center}
.quote{position:absolute;top:630px;width:100%;text-align:center;color:var(--white)}
.quote__title{font-size:27px}
.quote__lines{margin-top:14px;font-size:15px;line-height:1.6;font-weight:600}

/* cover */
.cover__title{position:absolute;top:640px;width:100%;text-align:center;color:var(--white);font-size:33px;line-height:1.15}
.cover__web{position:absolute;bottom:28px;width:100%;text-align:center;color:var(--white);font-weight:700;font-size:16px;letter-spacing:1px}

/* inside left */
.about{position:absolute;top:520px;left:30px;width:310px;color:var(--white)}
.about__title{font-size:28px;margin-bottom:10px}
.about p{font-size:12.5px;line-height:1.55;margin-bottom:10px}
.about strong{font-weight:700}

/* inside middle */
.services__title{position:absolute;top:150px;width:100%;text-align:center;font-size:26px;color:var(--red)}
.services__intro{position:absolute;top:194px;left:36px;width:298px;text-align:center}
.service-grid{position:absolute;top:300px;left:30px;width:310px;display:grid;grid-template-columns:repeat(3,1fr);row-gap:18px;text-align:center}
.service{display:flex;flex-direction:column;align-items:center;gap:6px;font-size:11.5px;font-weight:600;color:var(--ink)}
.service__icon{width:56px;height:56px;border-radius:50%;background:var(--red);display:flex;align-items:center;justify-content:center}
.spot{position:absolute;top:590px;width:108px;height:108px;border-radius:50%;border:4px solid var(--red)}

/* inside right */
.other{position:absolute;top:40px;left:34px;width:310px;color:var(--white)}
.other__title{font-size:26px;margin-bottom:14px}
.other ul{list-style:none}
.other li{font-size:13px;line-height:1.5;padding:5px 0 5px 18px;position:relative;border-bottom:1px solid rgba(255,255,255,.18)}
.other li::before{content:"";position:absolute;left:0;top:12px;width:8px;height:8px;background:var(--red);border-radius:50%}
</style>
</head>
<body>

<!-- OUTSIDE SPREAD -->
<section class="spread spread--outside">

  <article class="panel panel--reliable">
    <div class="photo" style="top:0;height:250px;background:linear-gradient(120deg,#2f5cab 0%,#9aa6bd 40%,#d8d3c0 70%,#e8c93c 100%)" role="img" aria-label="Photo of a mop and cleaning cart on an office floor"></div>
    <svg class="band" style="top:180px" height="110" viewBox="0 0 370 110" preserveAspectRatio="none">
      <path d="M0 40 Q185 110 370 30 L370 110 L0 110Z" fill="var(--paper)"/>
      <path d="M0 40 Q185 110 370 30" stroke="var(--red)" stroke-width="8" fill="none"/>
      <path d="M0 52 Q185 118 370 42" stroke="var(--blue)" stroke-width="4" fill="none"/>
    </svg>
    <h2 class="heading reliable__title">Reliable <span>Cleaning</span></h2>
    <div class="feature" style="top:352px">
      <div class="feature__icon"></div>
      <div><div class="feature__name">Green Products</div><p>We use safe, low-impact products that protect your family, pets and the planet every visit.</p></div>
    </div>
    <div class="feature" style="top:446px">
      <div class="feature__icon"></div>
      <div><div class="feature__name">Flexible Scheduling</div><p>Book a time that suits you, with weekly, biweekly or monthly visits available on request.</p></div>
    </div>
    <div class="feature" style="top:540px">
      <div class="feature__icon"></div>
      <div><div class="feature__name">Cleaning Done Right</div><p>Trained, insured crews follow a detailed checklist so every room is finished to our standard.</p></div>
    </div>
    <svg class="band" style="bottom:0" height="230" viewBox="0 0 370 230" preserveAspectRatio="none">
      <path d="M0 60 Q200 0 370 50 L370 230 L0 230Z" fill="var(--blue)"/>
      <path d="M0 150 Q150 120 240 170 L240 230 L0 230Z" fill="var(--red)"/>
    </svg>
    <p class="tagline">We like when it's<br>clean around!</p>
  </article>

  <article class="panel panel--contact">
    <svg class="band" style="top:0" height="260" viewBox="0 0 370 260" preserveAspectRatio="none">
      <path d="M0 0 H370 V190 Q185 250 0 200Z" fill="var(--red)"/>
      <path d="M0 206 Q185 256 370 196" stroke="var(--blue)" stroke-width="6" fill="none"/>
    </svg>
    <div class="contact__circle" role="img" aria-label="Photo of a vacuum cleaner on carpet"></div>
    <h2 class="heading contact__title">Contact Us</h2>
    <p class="body-text contact__text">We care about the safety of your home and the health of our world. Brightmoor Cleaning Services only uses eco-friendly products that are proven safe for the whole family, including children and pets.</p>
    <div class="logo" style="top:470px;left:60px;width:260px"><span class="logo__dot"></span><span>Brightmoor Cleaning Services</span></div>
    <svg class="band" style="bottom:0" height="290" viewBox="0 0 370 290" preserveAspectRatio="none">
      <path d="M0 50 Q185 0 370 40 L370 290 L0 290Z" fill="var(--blue)"/>
      <path d="M0 50 Q185 0 370 40" stroke="var(--red)" stroke-width="6" fill="none"/>
    </svg>
    <div class="quote">
      <h3 class="heading quote__title">Free Quote or Estimate!</h3>
      <div class="quote__lines">877-514-SHINE<br>472 Kestrel Ridge W Ste 518<br>Fernhollow, OR 98102</div>
    </div>
  </article>

  <article class="panel panel--cover">
    <div class="logo" style="top:40px;left:50px;width:280px;font-size:24px"><span class="logo__dot"></span><span>Brightmoor Cleaning Services</span></div>
    <svg class="band" style="top:130px" height="40" viewBox="0 0 370 40" preserveAspectRatio="none">
      <path d="M0 30 L370 5" stroke="var(--red)" stroke-width="6"/>
      <path d="M0 38 L370 13" stroke="var(--blue)" stroke-width="4"/>
    </svg>
    <div class="photo" style="top:165px;height:400px;background:linear-gradient(160deg,#e9e9ec 0%,#c8ccd6 40%,#5476b7 70%,#c9cdd6 100%)" role="img" aria-label="Photo of a cleaning crew wiping desks in a bright office"></div>
    <svg class="band" style="top:520px" height="340" viewBox="0 0 370 340" preserveAspectRatio="none">
      <path d="M0 70 L370 0 L370 340 L0 340Z" fill="var(--blue)"/>
      <path d="M0 62 L370 -8 L370 18 L0 88Z" fill="var(--red)"/>
      <path d="M0 88 L370 18" stroke="var(--white)" stroke-width="3"/>
    </svg>
    <h1 class="heading cover__title">Professional<br>Cleaning Services</h1>
    <div class="phone-pill" style="top:752px;left:58px">
      <span class="phone-pill__icon"><svg width="20" height="20" viewBox="0 0 24 24"><path d="M6.6 10.8a15 15 0 0 0 6.6 6.6l2.2-2.2a1 1 0 0 1 1-.25 11.4 11.4 0 0 0 3.6.57 1 1 0 0 1 1 1V20a1 1 0 0 1-1 1A17 17 0 0 1 3 4a1 1 0 0 1 1-1h3.5a1 1 0 0 1 1 1c0 1.25.2 2.45.57 3.57a1 1 0 0 1-.25 1z" fill="var(--red)"/></svg></span>
      877-514-SHINE
    </div>
    <div class="cover__web">www.brightmoorclean.com</div>
  </article>
</section>

<!-- INSIDE SPREAD -->
<section class="spread spread--inside">

  <article class="panel panel--about">
    <div class="photo" style="top:0;height:460px;background:linear-gradient(150deg,#4a4f5c 0%,#8a7460 45%,#c7b79c 70%,#3c5fa8 100%)" role="img" aria-label="Photo of a gloved hand polishing a conference table"></div>
    <svg class="band" style="top:400px" height="460" viewBox="0 0 370 460" preserveAspectRatio="none">
      <path d="M0 60 Q185 0 370 40 L370 460 L0 460Z" fill="var(--blue)"/>
      <path d="M0 60 Q185 0 370 40" stroke="var(--red)" stroke-width="8" fill="none"/>
      <path d="M0 70 Q185 12 370 50" stroke="var(--white)" stroke-width="3" fill="none"/>
    </svg>
    <div class="about">
      <h2 class="heading about__title">About Us</h2>
      <p>We understand life can be hectic and you may not have time to keep your home tidy let alone do a deeper clean.</p>
      <p>That's where <strong>Brightmoor Cleaning Services</strong> comes in. Our professional house cleaning service ensures your home is cleaned to your satisfaction. At your free in-home consultation, we'll discuss conducting an initial cleaning.</p>
      <p>The first cleaning will be important for ongoing maintenance while adhering to <strong>Brightmoor Cleaning Services</strong> standard of excellence. We offer the flexibility to schedule visits every week, every two weeks or monthly.</p>
    </div>
  </article>

  <article class="panel panel--services" style="background:var(--white)">
    <div class="logo" style="top:50px;left:60px;width:260px"><span class="logo__dot"></span><span>Brightmoor Cleaning Services</span></div>
    <h2 class="heading services__title">Our Services</h2>
    <p class="body-text services__intro">Whether you require a one-time or recurring cleaning for your house or apartment, we're available to personalize your service based on your needs.</p>
    <div class="service-grid">
      <div class="service"><span class="service__icon"></span>Carpet Cleaning</div>
      <div class="service"><span class="service__icon"></span>Floor Care</div>
      <div class="service"><span class="service__icon"></span>Janitorial Services</div>
      <div class="service"><span class="service__icon"></span>Window Cleaning</div>
      <div class="service"><span class="service__icon"></span>Sanitation Supplies</div>
    </div>
    <div class="spot" style="left:16px;background:linear-gradient(135deg,#d7d9de,#8e96a8)" role="img" aria-label="Photo of a carpet being vacuumed"></div>
    <div class="spot" style="left:131px;background:linear-gradient(135deg,#f2d64a,#e5e6ea)" role="img" aria-label="Photo of a gloved hand cleaning a surface"></div>
    <div class="spot" style="left:246px;background:linear-gradient(135deg,#c9a772,#7d6a55)" role="img" aria-label="Photo of a polished wooden floor"></div>
    <div class="phone-pill" style="top:740px;left:58px">
      <span class="phone-pill__icon"><svg width="20" height="20" viewBox="0 0 24 24"><path d="M6.6 10.8a15 15 0 0 0 6.6 6.6l2.2-2.2a1 1 0 0 1 1-.25 11.4 11.4 0 0 0 3.6.57 1 1 0 0 1 1 1V20a1 1 0 0 1-1 1A17 17 0 0 1 3 4a1 1 0 0 1 1-1h3.5a1 1 0 0 1 1 1c0 1.25.2 2.45.57 3.57a1 1 0 0 1-.25 1z" fill="var(--red)"/></svg></span>
      877-514-SHINE
    </div>
  </article>

  <article class="panel panel--other" style="background:var(--blue)">
    <div class="other">
      <h2 class="heading other__title">Other Services</h2>
      <ul>
        <li>Dry Area Services</li>
        <li>Construction Clean-Ups</li>
        <li>Quality Control Inspections</li>
        <li>Maid Services</li>
        <li>Light &amp; Ceiling Fixture Cleaning</li>
        <li>Wall Washing</li>
        <li>Drapery &amp; Blind Cleaning</li>
        <li>Acoustical Tile Cleaning</li>
        <li>Computer Terminal &amp; Keyboard Cleaning</li>
        <li>Marble, Granite &amp; Terrazzo Refinishing</li>
        <li>Power Washing</li>
      </ul>
    </div>
    <svg class="band" style="top:560px" height="80" viewBox="0 0 370 80" preserveAspectRatio="none">
      <path d="M0 60 Q185 0 370 20 L370 80 L0 80Z" fill="var(--white)"/>
      <path d="M0 60 Q185 0 370 20" stroke="var(--red)" stroke-width="8" fill="none"/>
    </svg>
    <div class="photo" style="top:620px;height:240px;background:linear-gradient(110deg,#e7e8ec 0%,#d24a5a 40%,#f0d040 60%,#4d7cc6 100%)" role="img" aria-label="Photo of cleaning bottles and supplies in a bucket"></div>
  </article>
</section>

</body>
</html>
```